Author and Publisher

Cover for a book on the process of publishing a book from the presentation to the publisher until the selling in bookstores :
A behind-the-scenes journey through the world of book publishing, from manuscript to bookstore. The book explores the relationship between authors and publishers, manuscript selection, contracts, editing, proofreading, book design, printing, distribution, bookstores and online sales. It reveals the many people, decisions and processes involved in turning a text into a physical book and bringing it to readers. The illustration should evoke publishing as a lively, contemporary ecosystem, combining creativity, craftsmanship, business and the enduring appeal of books.
FORMAT : 14 x 20,5 cm
AUTHOR : Luc Dorvasse
TITLE : Le veilleur et la rive
PUBLISHER : Editions Plumeaux (at the bottom of the page)
Target Market(s)
General public, mainly news authors of books
Look and feel

```html
<!DOCTYPE html>
<html lang="fr">
<head>
<meta charset="utf-8">
<title>Le veilleur et la rive — Luc Dorvasse</title>
<link rel="stylesheet" href="https://fonts.googleapis.com/css2?family=Antonio:wght@600;700&family=Zilla+Slab:wght@500;600&display=swap">
<style>
  :root {
    --page-bg: #d0d0d0;
    --paper: #fbfbfb;
    --ink-blue: #1f6cc4;
    --orange-hot: #f38a24;
    --orange-red: #e2452a;
    --rust-dark: #4e2318;
    --stripe: #fbfbfb;
  }
  * { margin: 0; padding: 0; box-sizing: border-box; }
  html, body {
    width: 1200px; height: 1200px; overflow: hidden;
    background: var(--page-bg);
  }
  .canvas {
    position: relative; width: 1200px; height: 1200px;
    display: flex; align-items: center; justify-content: center;
  }
  .cover {
    position: relative; width: 560px; height: 820px;
    background: var(--paper);
    box-shadow: 0 18px 40px rgba(0,0,0,0.18);
    overflow: hidden;
  }
  .cover__author {
    position: absolute; top: 48px; left: 0; right: 0;
    text-align: center;
    font-family: "Zilla Slab", serif; font-weight: 600;
    font-size: 44px; color: var(--ink-blue); letter-spacing: 1px;
  }
  .cover__field {
    position: absolute; top: 115px; left: 0; right: 0; bottom: 0;
    background:
      radial-gradient(ellipse 60% 45% at 45% 30%, rgba(243,138,36,0.95), rgba(243,138,36,0) 70%),
      radial-gradient(ellipse 55% 40% at 55% 82%, rgba(246,140,34,0.95), rgba(246,140,34,0) 75%),
      linear-gradient(90deg, var(--orange-red) 0%, var(--orange-hot) 45%, #e8701f 70%, var(--rust-dark) 100%);
  }
  .cover__grain {
    position: absolute; inset: 0; width: 100%; height: 100%;
    mix-blend-mode: overlay; opacity: 0.55;
  }
  .stripe {
    position: absolute; left: 0; right: 0; height: 12px;
    background: var(--stripe);
  }
  .stripe--1 { top: 150px; }
  .stripe--2 { top: 208px; }
  .stripe--3 { top: 290px; }
  .stripe--title { top: 400px; height: 13px; }
  .stripe--5 { top: 552px; }
  .cover__title {
    position: absolute; top: 322px; left: 0; right: 0;
    text-align: center;
    font-family: "Antonio", sans-serif; font-weight: 700;
    font-size: 64px; line-height: 80px; color: var(--stripe);
    letter-spacing: -0.5px; word-spacing: 4px; white-space: nowrap;
  }
  .cover__topics {
    position: absolute; top: 432px; left: 40px; right: 40px;
    text-align: center;
    font-family: "Zilla Slab", serif; font-weight: 600;
    font-size: 17px; line-height: 23px; color: var(--stripe);
  }
  .cover__topics .dot { color: var(--ink-blue); padding: 0 5px; }
  .cover__publisher {
    position: absolute; bottom: 48px; left: 0; right: 0;
    text-align: center;
    font-family: "Antonio", sans-serif; font-weight: 600;
    font-size: 22px; color: var(--stripe); letter-spacing: 0.3px;
  }
</style>
</head>
<body>
<main class="canvas">
  <article class="cover">
    <p class="cover__author">Luc Dorvasse</p>

    <div class="cover__field">
      <svg class="cover__grain" aria-hidden="true">
        <filter id="grain">
          <feTurbulence type="fractalNoise" baseFrequency="0.9" numOctaves="2" stitchTiles="stitch"/>
          <feColorMatrix type="saturate" values="0"/>
        </filter>
        <rect width="100%" height="100%" filter="url(#grain)"/>
      </svg>
    </div>

    <div class="stripe stripe--1"></div>
    <div class="stripe stripe--2"></div>
    <div class="stripe stripe--3"></div>
    <div class="stripe stripe--title"></div>
    <div class="stripe stripe--5"></div>

    <h1 class="cover__title">Le veilleur et la rive</h1>

    <p class="cover__topics">
      Publishers<span class="dot">•</span>Manuscript Selection<span class="dot">•</span>Contracts<br>
      Editing<span class="dot">•</span>Proofreading<span class="dot">•</span>Book Design<br>
      Printing<span class="dot">•</span>Distribution<span class="dot">•</span>Sales
    </p>

    <p class="cover__publisher">Publisher: Editions Plumeaux</p>
  </article>
</main>
</body>
</html>
```